Real Estate For Sale Sign

I need to design a for sale sign. It needs to include The following information
Logo: Attached
Name: Corinne Vasquel,
Company Name: Gilded Harbor Real Estate,
Phone Number: 503-841-2096
BRE Licence Number 04817359 (Can Be small)
Sign size 24x30

I am not sure about including my website but I would like to see options with it. www.gildedharbor-example.com
Updates

Target Market(s)

Potential Buyers or Sellers of Real Estate. Must be easy to read.

Industry/Entity Type

Real Estate

Requirements
Must have
• I want it to feel luxurious and sharp.

```html
<!DOCTYPE html>
<html lang="en">
<head>
<meta charset="utf-8">
<title>Gilded Harbor Real Estate – Luxury Homes Sign</title>
<link href="https://fonts.googleapis.com/css2?family=Marcellus&family=Oswald:wght@600;700&family=Arimo:wght@700&display=swap" rel="stylesheet">
<style>
  :root{
    --plum-deep:#230b33;
    --plum-mid:#4a1f66;
    --plum-light:#6a3490;
    --white:#ffffff;
    --gold:#f7c031;
    --gold-dark:#d99a16;
    --gold-light:#ffd968;
    --magenta:#c0399c;
    --brand:#2d557f;
    --ornament:#d9c6e6;
    --wall-light:#f6eedc;
    --wall-warm:#e6d0a6;
    --curtain:#c9a25e;
    --floor-light:#c97a3c;
    --floor-dark:#7e3f1b;
  }
  *{margin:0;padding:0;box-sizing:border-box}
  html,body{width:960px;height:1200px;overflow:hidden;background:var(--plum-deep)}
  .sign{
    position:relative;width:960px;height:1200px;overflow:hidden;
    background:radial-gradient(ellipse at 50% 45%, var(--plum-light) 0%, var(--plum-mid) 45%, var(--plum-deep) 100%);
    color:var(--white);text-align:center;
  }
  .headline{
    position:absolute;top:64px;left:0;width:100%;
    font-family:"Marcellus",serif;font-size:68px;line-height:78px;
    letter-spacing:1px;font-weight:400;
  }
  .tagline{
    position:absolute;top:220px;left:0;width:100%;
    font-family:"Oswald",sans-serif;font-weight:700;font-size:57px;
    color:var(--gold);letter-spacing:1.5px;line-height:66px;
  }
  .flourish{
    position:absolute;left:410px;width:140px;height:26px;
    background:linear-gradient(90deg,transparent,var(--ornament) 30%,var(--ornament) 70%,transparent);
    opacity:.45;border-radius:13px;
  }
  .flourish.top{top:312px}
  .flourish.bottom{top:856px}
  .showcase{position:absolute;left:144px;top:360px;width:672px;height:480px;overflow:visible}
  .brand-plate{
    position:absolute;left:340px;top:914px;width:280px;height:112px;
    background:var(--white);display:flex;align-items:center;justify-content:center;gap:12px;
  }
  .brand-mark{width:38px;height:38px;border-radius:50%;background:var(--brand);flex:none}
  .brand-name{
    font-family:"Marcellus",serif;font-weight:400;color:var(--brand);
    font-size:22px;line-height:26px;text-align:left;
  }
  .contact{
    position:absolute;left:0;width:100%;
    font-family:"Arimo",sans-serif;font-weight:700;font-size:21px;
    display:flex;justify-content:center;align-items:center;gap:14px;
  }
  .contact.name{top:1037px}
  .contact.reach{top:1076px}
  .contact.place{top:1116px}
  .item{display:flex;align-items:center;gap:7px;white-space:nowrap}
  .icon{width:22px;height:22px;flex:none}
  .licence{
    position:absolute;top:1152px;left:0;width:100%;
    font-family:"Arimo",sans-serif;font-weight:700;font-size:13px;
  }
</style>
</head>
<body>
<main class="sign">
  <h1 class="headline">LOOKING FOR A<br>LUXURIOUS HOME?</h1>
  <p class="tagline">WE'LL GIVE YOU THE BEST DEALS</p>

  <div class="flourish top" role="img" aria-label="Decorative scroll flourish"></div>

  <svg class="showcase" viewBox="0 0 672 480" xmlns="http://www.w3.org/2000/svg">
    <defs>
      <path id="frame-shape" d="M0,110 Q40,110 40,70 L150,70 Q170,70 180,40 Q200,0 260,0 L412,0 Q472,0 492,40 Q502,70 522,70 L632,70 Q632,110 672,110 L672,370 Q632,370 632,410 L522,410 Q502,410 492,440 Q472,480 412,480 L260,480 Q200,480 180,440 Q170,410 150,410 L40,410 Q40,370 0,370 Z"/>
      <linearGradient id="gold-band" x1="0" y1="0" x2="1" y2="1">
        <stop offset="0" stop-color="var(--gold-light)"/>
        <stop offset=".5" stop-color="var(--gold)"/>
        <stop offset="1" stop-color="var(--gold-dark)"/>
      </linearGradient>
      <linearGradient id="room-tone" x1="0" y1="0" x2="0" y2="1">
        <stop offset="0" stop-color="var(--wall-light)"/>
        <stop offset=".3" stop-color="var(--wall-warm)"/>
        <stop offset=".5" stop-color="var(--curtain)"/>
        <stop offset=".62" stop-color="var(--floor-light)"/>
        <stop offset="1" stop-color="var(--floor-dark)"/>
      </linearGradient>
      <radialGradient id="room-glow" cx=".5" cy=".35" r=".6">
        <stop offset="0" stop-color="#fffaf0" stop-opacity=".55"/>
        <stop offset=".6" stop-color="#fffaf0" stop-opacity="0"/>
        <stop offset="1" stop-color="#3a1a0a" stop-opacity=".35"/>
      </radialGradient>
      <filter id="frame-shadow" x="-10%" y="-10%" width="120%" height="120%">
        <feDropShadow dx="0" dy="4" stdDeviation="6" flood-color="#12041c" flood-opacity=".5"/>
      </filter>
    </defs>
    <use href="#frame-shape" fill="url(#gold-band)" filter="url(#frame-shadow)"/>
    <use href="#frame-shape" fill="var(--gold-dark)" transform="translate(336 240) scale(0.955) translate(-336 -240)"/>
    <g role="img" aria-label="Photo of an elegant living room with cream leather sofas, draped curtains, a patterned rug and polished wooden floor">
      <use href="#frame-shape" fill="url(#room-tone)" transform="translate(336 240) scale(0.945) translate(-336 -240)"/>
      <use href="#frame-shape" fill="url(#room-glow)" transform="translate(336 240) scale(0.945) translate(-336 -240)"/>
    </g>
    <use href="#frame-shape" fill="none" stroke="var(--white)" stroke-width="2.5" transform="translate(336 240) scale(0.9) translate(-336 -240)"/>
  </svg>

  <div class="flourish bottom" role="img" aria-label="Decorative scroll flourish"></div>

  <div class="brand-plate">
    <span class="brand-mark"></span>
    <span class="brand-name">Gilded Harbor<br>Real Estate</span>
  </div>

  <div class="contact name">
    <span class="item">
      <svg class="icon" viewBox="0 0 22 22"><circle cx="11" cy="11" r="11" fill="var(--magenta)"/><circle cx="11" cy="8" r="3.2" fill="var(--white)"/><path d="M5.5 16.5 Q11 10 16.5 16.5 Z" fill="var(--white)"/></svg>
      Corinne Vasquel
    </span>
  </div>

  <div class="contact reach">
    <span class="item">
      <svg class="icon" viewBox="0 0 22 22"><circle cx="11" cy="11" r="11" fill="var(--magenta)"/><path d="M7 5.5 L9.3 5.5 L10 8.6 L8.6 9.6 Q9.8 12.4 12.4 13.4 L13.4 12 L16.5 12.7 L16.5 15 Q16.5 16.5 15 16.5 Q6 15.8 5.5 7 Q5.5 5.5 7 5.5 Z" fill="var(--white)"/></svg>
      503-841-2096
    </span>
    <span class="item">
      <svg class="icon" viewBox="0 0 22 22"><circle cx="11" cy="11" r="11" fill="var(--magenta)"/><rect x="5" y="7" width="12" height="8.5" rx="1" fill="var(--white)"/><path d="M5.5 7.5 L11 11.8 L16.5 7.5" fill="none" stroke="var(--magenta)" stroke-width="1.3"/></svg>
      corinne@gildedharbor-example.com
    </span>
  </div>

  <div class="contact place">
    <span class="item">
      <svg class="icon" viewBox="0 0 22 22"><circle cx="11" cy="11" r="11" fill="var(--magenta)"/><g fill="none" stroke="var(--white)" stroke-width="1.4"><circle cx="11" cy="11" r="6"/><ellipse cx="11" cy="11" rx="2.6" ry="6"/><path d="M5 11 H17"/></g></svg>
      www.gildedharbor-example.com
    </span>
    <span class="item">
      <svg class="icon" viewBox="0 0 22 22"><path d="M11 1 C5.5 1 3 5 3 8.5 C3 13.5 11 21 11 21 C11 21 19 13.5 19 8.5 C19 5 16.5 1 11 1 Z" fill="var(--magenta)"/><circle cx="11" cy="8.5" r="3" fill="var(--white)"/></svg>
      2650 Lantern Quay Road, Portland, OR 97209
    </span>
  </div>

  <p class="licence">BRE Licence 04817359</p>
</main>
</body>
</html>
```